KEV.PRO- Darren Holcombe Fitness- needs a clever business card using the logo, name, info, contact

I need a business card designed for my Online Personal Training company called KEV.PRO, abbreviation for Darren Holcombe Fitness. My company focuses on coaching in personal health and personal growth to unleash your greatest potential. I would like to see designs that use my color scheme of a redish-orange (C:0,M:84,Y:100,K:0), grey, white, black, and my company font is OSWALD. The final design should communicate some aspects of design, health, motivation, growth, in some way. The logo is very important to the company and can be displayed in any of the colors previously mentioned. Must include the company name, my website: www.kev-pro.example , my email: dan@kev-pro.example

Target Market(s)

Personal health, fitness, general public, those who lack knowledge, awareness, and confidence in personal health

Industry/Entity Type

Personal Trainer

Font styles to use
Other font styles liked:
• OSWALD. (Bold, Regular, Light)

Colors
f37122
ffffff
9d9d9d
000000

Requirements
Must have
• Must include the logo, company name, my website: www.kev-pro.example , my email: dan@kev-pro.example
Nice to have
• Variations of the colors scheme of a redish-orange (C:0,M:84,Y:100,K:0), grey, white, black. Logo, card, or text can be in any of these colors.
• Possible quote like "Take control of your personal health to unleash your greatest potential" or "Unleashing your greatness first begins with fitness of the body and mind"

```html
<!DOCTYPE html>
<html lang="en">
<head>
<meta charset="utf-8">
<title>KEV.PRO Business Card</title>
<link rel="stylesheet" href="https://fonts.googleapis.com/css2?family=Oswald:wght@300;400;700&family=Open+Sans:ital,wght@1,400&display=swap">
<style>
  :root {
    --brand-orange: #f37122;
    --white: #ffffff;
    --grey: #9d9d9d;
    --black: #000000;
    --card: #0d0d0d;
    --backdrop: #3a332f;
    --divider: #d8d8d8;
  }
  * { margin: 0; padding: 0; box-sizing: border-box; }
  html, body { width: 1200px; height: 864px; overflow: hidden; }
  body {
    background: var(--backdrop);
    font-family: 'Oswald', sans-serif;
    position: relative;
  }
  .card {
    position: absolute;
    width: 540px;
    height: 308px;
    background: var(--card);
    border-radius: 3px;
    box-shadow: 0 14px 34px rgba(0,0,0,0.55);
    overflow: hidden;
  }

  /* Back of card */
  .card-back { left: 70px; top: 100px; }
  .back-mark {
    position: absolute;
    left: 170px; top: 40px;
    display: flex; align-items: center; gap: 18px;
  }
  .back-mark .mark-circle {
    width: 120px; height: 120px;
    border: 6px solid #5c5c5c;
    border-radius: 50%;
  }
  .back-mark .mark-name {
    font-weight: 700;
    font-size: 44px;
    color: #5c5c5c;
    letter-spacing: 1px;
  }
  .back-quote {
    position: absolute;
    left: 40px; top: 198px;
    font-family: 'Open Sans', sans-serif;
    font-style: italic;
    font-size: 15px;
    line-height: 1.5;
    color: var(--grey);
  }

  /* Front of card */
  .card-front { left: 590px; top: 470px; }
  .brand-block {
    position: absolute;
    left: 40px; top: 78px;
    width: 200px;
    display: flex; flex-direction: column; align-items: center;
  }
  .brand-circle {
    width: 104px; height: 104px;
    border: 6px solid var(--brand-orange);
    border-radius: 50%;
    margin-bottom: 12px;
  }
  .brand-name {
    font-weight: 700;
    font-size: 30px;
    line-height: 1;
    color: var(--white);
    letter-spacing: 0.5px;
  }
  .brand-tagline {
    font-weight: 300;
    font-size: 9px;
    color: var(--white);
    text-transform: uppercase;
    letter-spacing: 0.4px;
    margin-top: 3px;
  }
  .divider {
    position: absolute;
    left: 268px; top: 40px;
    width: 2px; height: 228px;
    background: linear-gradient(to bottom, transparent, var(--divider) 30%, var(--divider) 70%, transparent);
  }
  .contact-block {
    position: absolute;
    left: 300px; top: 92px;
  }
  .person-name {
    font-weight: 700;
    font-size: 22px;
    color: var(--brand-orange);
    text-transform: uppercase;
    line-height: 1.1;
  }
  .person-role {
    font-weight: 400;
    font-size: 16px;
    color: var(--white);
    text-transform: uppercase;
    margin-bottom: 18px;
  }
  .contact-list { list-style: none; }
  .contact-list li {
    display: flex; align-items: center; gap: 10px;
    font-weight: 400;
    font-size: 16px;
    color: var(--white);
    line-height: 1.55;
  }
  .contact-list svg { width: 13px; height: 13px; fill: var(--brand-orange); flex-shrink: 0; }
</style>
</head>
<body>

  <section class="card card-back">
    <div class="back-mark">
      <div class="mark-circle"></div>
      <div class="mark-name">KEV.PRO</div>
    </div>
    <p class="back-quote">
      Take control of your personal health to unleash your greatest potential<br>
      Unleashing your greatness first begins with fitness of the body and mind
    </p>
  </section>

  <section class="card card-front">
    <div class="brand-block">
      <div class="brand-circle"></div>
      <div class="brand-name">KEV.PRO</div>
      <div class="brand-tagline">Darren Holcombe Fitness</div>
    </div>
    <div class="divider"></div>
    <div class="contact-block">
      <div class="person-name">Alex Rowan</div>
      <div class="person-role">CEO/Founder</div>
      <ul class="contact-list">
        <li>
          <svg viewBox="0 0 24 24" aria-hidden="true"><path d="M6.6 10.8a15.1 15.1 0 0 0 6.6 6.6l2.2-2.2c.3-.3.7-.4 1-.2 1.1.4 2.3.6 3.6.6.6 0 1 .4 1 1V20c0 .6-.4 1-1 1A17 17 0 0 1 3 4c0-.6.4-1 1-1h3.5c.6 0 1 .4 1 1 0 1.3.2 2.5.6 3.6.1.3 0 .7-.2 1z"/></svg>
          555 014 2290
        </li>
        <li>
          <svg viewBox="0 0 24 24" aria-hidden="true"><path d="M2 5h20v14H2z M4 7v.5l8 5 8-5V7l-8 5z" fill-rule="evenodd"/></svg>
          dan@kev-pro.example
        </li>
        <li>
          <svg viewBox="0 0 24 24" aria-hidden="true"><circle cx="12" cy="12" r="10"/></svg>
          www.kev-pro.example
        </li>
      </ul>
    </div>
  </section>

</body>
</html>
```